New Personal Trainer needs poster to attract clients

Hi I am a personal trainer working inside a busy gym. My sole base of clients is from the gym itself where I compete with other trainers for business.
New company so my brand is still not noticed by the public.
My company name is Stridewell PT.
I am looking for a poster that will attract attention and increase awareness of my brand. My market will be mostly overweight men/women aged from 25-55 years old.
I would like pics of some sort on there that would be appropriate for my target market. Design needs to be colorful to attract attention.

My name and number must be added as well as facebook details
Dean Harlow
0437290518
(Facebook Symbol) Dean Harlow PT

Target Market(s)

Overweight men and women aged 25-55 years. Some would be mothers with young children

Industry/Entity Type

Fitness

Font styles to use
Sans Serif

Requirements
Must have
• My Logo.
• Pictures.
• Bright Attractive colours
• My name and number
• Slogan
Nice to have
• Slogan I'm leaning towards is "Building a Better You" but open to any ideas with this.

```html
<!DOCTYPE html>
<html lang="en">
<head>
<meta charset="utf-8">
<title>Stridewell PT – Dean Harlow Personal Trainer Poster</title>
<link rel="stylesheet" href="https://fonts.googleapis.com/css2?family=Roboto+Condensed:wght@400;700;900&family=Roboto:wght@400&display=swap">
<style>
  :root {
    --stage: #d6d6d6;
    --navy: #0d2130;
    --blue: #1e8fd6;
    --yellow: #ffe100;
    --white: #ffffff;
    --ink: #0b0b0b;
    --orange: #f39a1e;
    --social: #3b5a9a;
  }
  * { box-sizing: border-box; margin: 0; padding: 0; }
  html, body {
    width: 1000px; height: 1200px; overflow: hidden;
    background: var(--stage);
  }
  .poster {
    position: absolute; left: 59px; top: 13px;
    width: 882px; height: 1174px;
    background: var(--white);
    overflow: hidden;
    font-family: "Roboto Condensed", Arial, sans-serif;
  }
  .poster__shapes { position: absolute; inset: 0; }
  .brand {
    position: absolute; right: 40px; top: 32px;
    font-weight: 900; font-size: 42px; letter-spacing: 1px;
    color: var(--yellow); line-height: 1;
  }
  .trainer-name {
    position: absolute; right: 40px; top: 100px;
    text-align: right; color: var(--white);
    font-family: "Roboto", Arial, sans-serif;
    font-size: 76px; line-height: 72px; font-weight: 400;
  }
  .trainer-role {
    position: absolute; right: 40px; top: 258px;
    color: var(--white); font-size: 25px; letter-spacing: 3px;
  }
  .slogan {
    position: absolute; left: 470px; width: 420px; top: 350px;
    text-align: center; color: var(--ink);
    font-weight: 900; font-size: 68px; line-height: 64px;
  }
  .prompt {
    position: absolute; left: 470px; width: 420px; top: 578px;
    text-align: center; color: var(--ink);
    font-family: "Roboto", Arial, sans-serif; font-size: 34px; line-height: 34px;
  }
  .cta {
    position: absolute; left: 490px; top: 672px;
    width: 392px; height: 98px;
    background: var(--yellow); border-radius: 49px 0 0 49px;
    display: flex; align-items: center; justify-content: center;
    text-align: center; color: var(--ink);
    font-weight: 700; font-size: 36px; line-height: 36px;
  }
  .contact {
    position: absolute; left: 470px; display: flex; align-items: center; gap: 14px;
    color: var(--ink); font-size: 48px; line-height: 1;
  }
  .contact--phone { top: 798px; }
  .contact--social { top: 866px; font-size: 44px; }
  .contact__icon { width: 38px; height: 38px; flex: none; }
</style>
</head>
<body>
<main class="poster">
  <svg class="poster__shapes" width="882" height="1174" viewBox="0 0 882 1174">
    <defs>
      <linearGradient id="waistPhoto" x1="0" y1="0" x2="0" y2="1">
        <stop offset="0" stop-color="#f6eef0"/><stop offset="1" stop-color="#caa9b3"/>
      </linearGradient>
      <linearGradient id="trainerPhoto" x1="0" y1="0" x2="1" y2="1">
        <stop offset="0" stop-color="#142a3e"/><stop offset="0.5" stop-color="#6a4632"/><stop offset="1" stop-color="#142a3e"/>
      </linearGradient>
      <linearGradient id="backPhoto" x1="0" y1="0" x2="0" y2="1">
        <stop offset="0" stop-color="#2b3550"/><stop offset="1" stop-color="#b8696a"/>
      </linearGradient>
      <linearGradient id="curlPhoto" x1="0" y1="0" x2="1" y2="1">
        <stop offset="0" stop-color="#2a3346"/><stop offset="1" stop-color="#8a5d45"/>
      </linearGradient>
      <linearGradient id="dumbbellPhoto" x1="0" y1="0" x2="0" y2="1">
        <stop offset="0" stop-color="#f4efec"/><stop offset="1" stop-color="#c9a58e"/>
      </linearGradient>
    </defs>

    <rect class="photo photo--waist" x="0" y="0" width="320" height="290" fill="url(#waistPhoto)" role="img" aria-label="Photo of a woman measuring her waist with a tape"/>

    <polygon class="header-panel" points="420,0 882,0 882,312 450,312 370,156" fill="var(--navy)"/>
    <polygon class="chevron chevron--outer" points="300,0 360,0 280,150 360,300 300,300 220,150" fill="var(--blue)"/>
    <polygon class="chevron chevron--inner" points="380,0 430,0 350,150 430,300 380,300 300,150" fill="var(--blue)" opacity="0.85"/>

    <polygon class="accent-band" points="0,278 440,278 452,312 882,312 882,334 0,334" fill="var(--yellow)"/>

    <polygon class="frame-line" points="0,320 448,320 478,590 318,800 0,800" fill="var(--blue)"/>
    <polygon class="photo photo--trainer" points="0,334 432,334 460,588 306,788 0,788" fill="url(#trainerPhoto)" role="img" aria-label="Photo of a muscular personal trainer"/>

    <polygon class="frame-line frame-line--lower" points="360,790 404,790 668,1174 624,1174" fill="var(--navy)"/>
    <polygon class="photo photo--back" points="0,800 298,800 262,1174 0,1174" fill="url(#backPhoto)" role="img" aria-label="Photo of a woman training her back on a pulldown machine"/>
    <polygon class="photo photo--curl" points="312,800 372,800 620,1174 276,1174" fill="url(#curlPhoto)" role="img" aria-label="Photo of a man doing dumbbell curls"/>
    <rect class="photo photo--dumbbells" x="680" y="960" width="202" height="214" fill="url(#dumbbellPhoto)" role="img" aria-label="Photo of a fit woman holding dumbbells"/>
  </svg>

  <div class="brand">STRIDEWELL PT</div>
  <h1 class="trainer-name">DEAN<br>HARLOW</h1>
  <div class="trainer-role">PERSONAL TRAINER</div>

  <h2 class="slogan">BUILDING<br>A BETTER<br>YOU!</h2>
  <p class="prompt">Ready to make<br>the commitment?</p>
  <div class="cta">CONTACT DEAN<br>TODAY!</div>

  <div class="contact contact--phone">
    <svg class="contact__icon" viewBox="0 0 38 38" aria-hidden="true">
      <circle cx="19" cy="19" r="19" fill="var(--orange)"/>
      <path d="M12 10c1-1 2.5-1 3.2 0l2 3c.6.9.3 2-.5 2.6l-1 .8c.9 2.2 2.6 3.9 4.8 4.8l.8-1c.6-.8 1.7-1.1 2.6-.5l3 2c1 .7 1 2.2 0 3.2l-1.4 1.4c-1.2 1.2-3 1.4-4.6.7-4.4-2-7.9-5.5-9.9-9.9-.7-1.6-.5-3.4.7-4.6z" fill="var(--white)"/>
    </svg>
    <span>0437290518</span>
  </div>
  <div class="contact contact--social">
    <svg class="contact__icon" viewBox="0 0 38 38" aria-hidden="true">
      <circle cx="19" cy="19" r="19" fill="var(--social)"/>
    </svg>
    <span>Dean Harlow PT</span>
  </div>
</main>
</body>
</html>
```